Optometric Practice needs Initial Photoshop Mockup

We need a graphic design for the homepage of a website for an optometric practice that specializes in vision therapy.

Here's the link to the project folder on Filecove. I've included photos, example sites, content and instructions.

https://www.filecove.net/sh/qk7tmd3wz8rb2n5/BBX_HrLpVaQyJk6mTcDRZeNu

Please feel free to submit any questions about the design. I'll be happy to help guide you in any areas you're uncertain of.

Okay - I've updated the project to payment confirmed. Let's see some designs :) Thanks, Wes

```html
<!DOCTYPE html>
<html lang="en">
<head>
<meta charset="utf-8">
<title>ORVA – Optic Renewal Vision Associates</title>
<link href="https://fonts.googleapis.com/css2?family=Arimo:wght@400;700&family=Josefin+Sans:wght@400;600&family=Roboto+Condensed:wght@400;700&display=swap" rel="stylesheet">
<style>
:root{
  --brand-red:#a30d0d;
  --brand-red-dark:#8c0a0a;
  --navy:#2b2f8f;
  --text:#333;
  --text-soft:#555;
  --page-bg:#f2f2f2;
  --panel:#fafafa;
  --line:#bdbdbd;
  --footer:#464646;
  --footer-bottom:#1f1f1f;
  --white:#fff;
}
*{box-sizing:border-box;margin:0;padding:0}
html,body{width:950px;height:1200px;overflow:hidden}
body{position:relative;background:var(--page-bg);font-family:"Arimo",Arial,sans-serif;color:var(--text)}
.abs{position:absolute}

/* header */
.site-header{left:0;top:0;width:950px;height:120px;background:var(--white)}
.brand{left:82px;top:28px}
.brand-name{font-family:"Arimo",Arial,sans-serif;font-weight:700;font-size:38px;letter-spacing:4px;color:var(--brand-red);line-height:1}
.brand-tagline{font-size:9px;color:var(--navy);margin-top:4px;line-height:11px}
.social-top{right:82px;top:30px;display:flex;gap:12px}
.social-top span{display:flex;align-items:center;gap:4px;font-size:10px;color:#444}
.social-top i{width:12px;height:12px;border-radius:50%;display:block}
.phone-top{right:78px;top:80px;display:flex;align-items:center;gap:8px;font-size:20px;color:#222}

/* nav */
.main-nav{left:0;top:120px;width:950px;height:28px;background:var(--brand-red)}
.main-nav ul{list-style:none;position:absolute;left:83px;width:785px;top:0;height:28px;display:flex;justify-content:space-between;align-items:center}
.main-nav li{font-family:"Roboto Condensed",Arial,sans-serif;font-size:11px;color:var(--white);position:relative;height:28px;line-height:28px}
.main-nav li.active::after{content:"";position:absolute;left:50%;bottom:0;margin-left:-4px;border:4px solid transparent;border-bottom-color:var(--white)}

/* hero */
.hero{left:0;top:148px;width:950px;height:305px;background:linear-gradient(90deg,#e9e9e9 0%,#cfcfcf 35%,#bfc7cf 55%,#6d8cb3 75%,#46484c 100%)}
.hero-arrow{top:111px;width:35px;height:35px;border-radius:50%;background:rgba(40,40,40,.75)}
.hero-caption{left:0;top:263px;width:950px;height:42px;background:rgba(30,30,30,.8);color:var(--white);padding:5px 0 0 79px}
.hero-caption h2{font-size:13px;font-weight:700;letter-spacing:.2px}
.hero-caption p{font-size:10px;margin-top:2px}

/* welcome panel */
.welcome{left:78px;top:475px;width:518px;height:478px;background:var(--panel);border:1px solid #e6e6e6}
.welcome h1{position:absolute;left:13px;top:7px;font-family:"Josefin Sans",Arial,sans-serif;font-weight:400;font-size:21px;color:#111}
.welcome h1 em{font-style:normal;color:var(--brand-red)}
.rule{border-top:1px dotted var(--line)}
.welcome .rule{position:absolute;left:13px;width:472px;top:33px}
.welcome .intro{position:absolute;left:13px;top:45px;width:492px;font-size:9.5px;line-height:16px;color:var(--text-soft)}
.welcome .intro p+p{margin-top:15px}
.features-rule{position:absolute;left:16px;width:482px;top:229px;border-top:1px solid #ccc}
.feature-divider{position:absolute;left:252px;top:242px;height:220px;border-left:1px dotted var(--line)}
.feature{position:absolute;display:flex;gap:10px;width:236px}
.feature svg{flex:none}
.feature h3{font-size:10.5px;font-weight:700;color:#222;line-height:13px}
.feature p{font-size:9px;color:var(--text-soft);line-height:13px;margin-top:3px}
.feature-sep{position:absolute;border-top:1px dotted var(--line);width:230px}

/* sidebar */
.sidebar{left:620px;top:473px;width:250px;height:487px;background:var(--panel);border:1px solid #e6e6e6}
.sidebar h2{position:absolute;left:23px;font-family:"Josefin Sans",Arial,sans-serif;font-weight:400;font-size:16px;color:#111}
.video{left:24px;top:46px;width:201px;height:164px;background:linear-gradient(135deg,#5a3a28,#a66a4a 45%,#3d2c4a);border:1px solid #222}
.video-play{left:85px;top:62px;width:32px;height:32px;background:rgba(20,20,20,.8)}
.video-bar{left:6px;bottom:4px;width:189px;height:12px;background:#eee;font-size:6px;color:#333;display:flex;align-items:center;gap:6px;padding:0 4px}
.video-bar b{flex:1;height:2px;background:#999}
.banner-box{left:20px;top:272px;width:209px;height:182px;background:var(--white);border:1px solid #bbb}
.banner-head{font-size:7.5px;color:#333;background:#eef0f5;padding:4px 3px;border-bottom:1px solid #ccd}
.banner-page{display:flex;gap:4px;padding:5px 6px}
.banner-page .ph{width:35px;height:35px;background:#c9b7a7}
.banner-page strong{font-size:9px;color:#3b5998;line-height:11px;display:block}
.like-btn{display:inline-block;margin-top:3px;width:34px;height:12px;background:#5b74a8}
.banner-count{font-size:7px;color:#666;padding:0 6px;line-height:10px}
.banner-count span{color:#3b5998}
.faces{display:grid;grid-template-columns:repeat(5,35px);gap:2px;padding:5px 6px}
.faces i{height:35px;display:block;background:#b7b0a8}

/* footer */
.site-footer{left:0;top:999px;width:950px;height:176px;background:var(--footer);color:#eee}
.footer-brand{left:78px;top:62px;font-weight:700;font-size:36px;letter-spacing:4px;color:var(--white)}
.footer-col h2{font-size:16px;font-weight:400;color:var(--white);margin-bottom:6px}
.footer-col li{list-style:none;font-size:11px;line-height:22px;display:flex;align-items:center;gap:8px}
.footer-col li i{width:14px;height:14px;display:block;border-radius:2px}
.footer-col address{font-style:normal;font-size:11px;line-height:17.5px}
.field{display:block;width:138px;height:17px;background:var(--white);border-radius:3px;margin-bottom:8px}
.field.tall{height:36px}
.send{display:inline-block;width:51px;height:18px;background:var(--brand-red);color:var(--white);font-size:12px;text-align:center;line-height:18px}
.copyright{left:0;top:1175px;width:950px;height:25px;background:var(--footer-bottom);color:var(--white);font-size:10px;text-align:center;line-height:25px}
</style>
</head>
<body>

<header class="site-header abs">
  <div class="brand abs">
    <div class="brand-name">ORVA</div>
    <div class="brand-tagline">Optic Renewal<br>Vision Associates</div>
  </div>
  <div class="social-top abs">
    <span><i style="background:#3b5998"></i>Friendlane</span>
    <span><i style="background:#2aa3e0"></i>Chirpline</span>
    <span><i style="background:#1a75b8"></i>Workweave</span>
    <span><i style="background:#d32f2f"></i>Reelcast</span>
  </div>
  <div class="phone-top abs">
    <svg width="18" height="14" viewBox="0 0 18 14"><path d="M1 5c0-3 4-4 8-4s8 1 8 4l-3 1-1-2H5L4 6z" fill="var(--navy)"/><rect x="4" y="7" width="10" height="6" rx="1" fill="var(--navy)"/></svg>
    410-555-0148
  </div>
</header>

<nav class="main-nav abs">
  <ul>
    <li class="active">HOME</li><li>MEET US</li><li>NEW PATIENTS</li><li>VISION &amp; LEARNING</li><li>VISION THERAPY</li><li>BINOCULAR VISION DISORDERS</li><li>HEAD INJURIES</li><li>PROFESSIONALS</li><li>CONTACT US</li>
  </ul>
</nav>

<section class="hero abs" role="img" aria-label="Photo of an optometrist examining a teenage patient with a slit lamp">
  <div class="hero-arrow abs" style="left:42px"><svg width="35" height="35"><path d="M20 10l-7 7.5 7 7.5" stroke="#fff" fill="none" stroke-width="1.5"/></svg></div>
  <div class="hero-arrow abs" style="left:871px"><svg width="35" height="35"><path d="M15 10l7 7.5-7 7.5" stroke="#fff" fill="none" stroke-width="1.5"/></svg></div>
  <div class="hero-caption abs">
    <h2>&#9679; IMPROVING VISION, CHANGING LIVES</h2>
    <p>HAPPY KIDS, OR A COLLAGE OF THEIR PHOTOS OF KIDS GETTING VISION THERAPY</p>
  </div>
</section>

<main class="welcome abs">
  <h1>WELCOME TO <em>ORVA</em></h1>
  <div class="rule"></div>
  <div class="intro">
    <p>There are many visual skills critical for reading and learning. Often, a vision problem is misdiagnosed as an attention problem or a learning disability due to similarity of symptoms. Anyone who is struggling with reading, has poor reading comprehension, or just isn't performing to their full potential, should consider scheduling a developmental vision evaluation. To help determine if you or your child should be tested, Do the Checklist on our Vision Quiz page.</p>
    <p>Dr. Daniel Marrow is a developmental optometrist who specializes in the diagnosis and treatment of vision problems that interfere with reading and learning. He is a member of the National Optometric Society, the Guild of Developmental Vision Practitioners, and a Fellow in the Academy of Clinical Eye Care. The Clear Sight Learning Centers and Dr. Daniel Marrow provide.</p>
  </div>
  <div class="features-rule"></div>
  <div class="feature-divider"></div>

  <div class="feature" style="left:16px;top:255px">
    <svg width="42" height="30" viewBox="0 0 42 30"><path d="M2 15C10 4 32 4 40 15C32 26 10 26 2 15z" fill="none" stroke="#111" stroke-width="2.5"/><circle cx="21" cy="15" r="7" fill="none" stroke="#111" stroke-width="2.5"/><circle cx="21" cy="15" r="3" fill="#111"/></svg>
    <div><h3>Improving Vision, Changing Lives</h3><p>Happy kids, or a collage of their photos of kids getting Vision Therapy.</p></div>
  </div>
  <div class="feature" style="left:265px;top:255px">
    <svg width="42" height="40" viewBox="0 0 42 40"><path d="M21 6a10 10 0 0 0-6 18v5h12v-5a10 10 0 0 0-6-18z" fill="none" stroke="#111" stroke-width="2"/><path d="M17 32h8M18 35h6M21 1v3M8 7l2 2M34 7l-2 2M4 17h3M35 17h3" stroke="#111" stroke-width="2"/></svg>
    <div><h3>Bright Child Struggling with Reading It could be a vision problem</h3><p>(picture of a child having trouble learning or reading)</p></div>
  </div>
  <div class="feature-sep" style="left:16px;top:316px"></div>
  <div class="feature-sep" style="left:265px;top:316px"></div>

  <div class="feature" style="left:16px;top:328px">
    <svg width="42" height="42" viewBox="0 0 42 42"><rect x="5" y="28" width="4" height="12" fill="#111"/><rect x="12" y="24" width="4" height="16" fill="#111"/><rect x="19" y="20" width="4" height="20" fill="#111"/><rect x="26" y="16" width="4" height="24" fill="#111"/><rect x="33" y="12" width="4" height="28" fill="#111"/><path d="M4 24L30 6" stroke="#111" stroke-width="3"/><path d="M24 4h10v10" fill="none" stroke="#111" stroke-width="3"/></svg>
    <div><h3>Improve Your Sports Performance</h3><p>(picture of a child or adult doing a sport that requires hand/eye coordination)</p></div>
  </div>
  <div class="feature" style="left:265px;top:330px">
    <svg width="42" height="36" viewBox="0 0 42 36"><rect x="6" y="3" width="30" height="30" rx="3" fill="none" stroke="#111" stroke-width="2.5"/><path d="M12 11h14M12 17h18M12 23h10" stroke="#111" stroke-width="2.5"/></svg>
    <div><h3>Is it really ADD/ADHD?</h3><p>(picture of child having trouble learning, or distracted)</p></div>
  </div>
  <div class="feature-sep" style="left:16px;top:388px"></div>
  <div class="feature-sep" style="left:265px;top:388px"></div>

  <div class="feature" style="left:16px;top:402px">
    <svg width="46" height="30" viewBox="0 0 46 30"><circle cx="12" cy="15" r="9" fill="none" stroke="#111" stroke-width="2.5"/><circle cx="34" cy="15" r="9" fill="none" stroke="#111" stroke-width="2.5"/><path d="M21 14q2-3 4 0" fill="none" stroke="#111" stroke-width="2.5"/></svg>
    <div><h3>Improve Your Vision at Any Age</h3><p>(picture of adult(s) studying)</p></div>
  </div>
  <div class="feature" style="left:265px;top:400px">
    <svg width="42" height="34" viewBox="0 0 42 34"><path d="M8 16C14 7 28 7 34 16C28 25 14 25 8 16z" fill="none" stroke="#111" stroke-width="2.5"/><circle cx="21" cy="16" r="4" fill="#111"/><path d="M3 14v12l8 6M39 14v12l-8 6" fill="none" stroke="#111" stroke-width="3"/></svg>
    <div><h3>There is more to healthy vision that 20/20 eyesight</h3><p>(picture of someone reading)</p></div>
  </div>
</main>

<aside class="sidebar abs">
  <h2 style="top:14px">FEATURED VIDEO</h2>
  <div class="rule abs" style="left:23px;top:35px;width:232px"></div>
  <div class="video abs" role="img" aria-label="Still frame of a news presenter from a featured video interview">
    <div class="video-play abs"><svg width="32" height="32"><path d="M12 9l11 7-11 7z" fill="#fff"/></svg></div>
    <div class="video-bar abs">&#9654; 00:00 <b></b> 00:00</div>
  </div>
  <div class="abs" style="left:14px;top:229px;width:237px;border-top:1px solid #ccc"></div>
  <h2 style="top:242px">SIDE BANNERS</h2>
  <div class="banner-box abs">
    <div class="banner-head">Find us on Friendlane</div>
    <div class="banner-page">
      <div class="ph" role="img" aria-label="Profile photo of the practice's optometrist"></div>
      <div><strong>ORVA: Dr. Daniel Marrow, Developmental Optometrist</strong><span class="like-btn"></span></div>
    </div>
    <p class="banner-count">155 people like <span>ORVA: Dr. Daniel Marrow, Developmental Optometrist.</span></p>
    <div class="faces" role="img" aria-label="Grid of small profile photos of page followers">
      <i></i><i style="background:#a59e96"></i><i style="background:#c3b2a4"></i><i style="background:#8d96a3"></i><i style="background:#dde0e4"></i>
      <i style="background:#d98a3a"></i><i style="background:#a99f97"></i><i style="background:#8a9a78"></i><i style="background:#c9c2b8"></i><i style="background:#b49a86"></i>
    </div>
  </div>
</aside>

<footer class="site-footer abs">
  <div class="footer-brand abs">ORVA</div>
  <div class="footer-col abs" style="left:309px;top:20px">
    <h2>Social media</h2>
    <ul>
      <li><i style="background:#3b5998"></i>Follow us Friendlane</li>
      <li><i style="background:#2aa3e0"></i>Follow us Chirpline</li>
      <li><i style="background:#1a75b8"></i>Follow us Workweave</li>
      <li><i style="background:#d32f2f"></i>Reelcast</li>
    </ul>
  </div>
  <div class="footer-col abs" style="left:488px;top:20px">
    <h2>Addresses</h2>
    <address>The Clear Sight Learning Centers<br>Dr. Daniel Marrow<br>18 Linden Ave. Suite 200, Room 3<br>Harwood, MD, 21099<br>Phone: 410-555-0148</address>
  </div>
  <div class="footer-col abs" style="left:727px;top:20px">
    <h2>contact information</h2>
    <span class="field"></span><span class="field"></span><span class="field tall"></span>
    <span class="send">Send</span>
  </div>
</footer>
<div class="copyright abs">© 2012 Orva, Inc. All rights reserved.</div>

</body>
</html>
```